Business card

We are looking for a creative person to deigns our company business card.

Target Market(s)

College age student

Industry/Entity Type

Accommodation

Contact Information for Business Card

We want a fun, clean and sophisticated design. It should look good, but more importantly the information should be legible.

Font styles to use
Serif
Sans Serif
Other font styles liked:
• Open Sans ,

Colors
33a6d7

Requirements
Must have
• Must have a young and memorable message. Be legible.
• Our logo on the back on a solid blue , please find color and logo attached
• LodgeBridgely.net on the back.
Nice to have
• I would like to have couple of different fonts on the LodgeBridgely.net on the back of the cards with a solid blue.

```html
<!DOCTYPE html>
<html lang="en">
<head>
<meta charset="utf-8">
<title>LodgeBridgely Business Card</title>
<link rel="stylesheet" href="https://fonts.googleapis.com/css2?family=Open+Sans:wght@400;700&family=PT+Serif:wght@700&display=swap">
<style>
  :root {
    --page: #ffffff;
    --card-white: #ffffff;
    --royal: #105bd4;
    --bright: #2f7ff9;
    --deep: #0356e0;
    --sky: #33a6d7;
    --aqua: #27b0e0;
    --navy: #0d3f70;
    --ink: #111111;
    --edge: #2aa5f2;
  }
  * { box-sizing: border-box; margin: 0; padding: 0; }
  html, body { width: 1200px; height: 1200px; overflow: hidden; background: var(--page); }
  .canvas { position: relative; width: 1200px; height: 1200px; }

  .card { position: absolute; overflow: hidden; }
  .card-front {
    left: 192px; top: 60px; width: 806px; height: 466px;
    background: var(--card-white);
    border: 1px solid var(--edge);
  }
  .card-back {
    left: 192px; top: 607px; width: 816px; height: 467px;
    background: var(--royal);
  }

  .wave-area { position: absolute; left: 0; top: 0; width: 100%; height: 100%; }

  .contact-list { position: absolute; left: 301px; top: 89px; list-style: none; }
  .contact-item {
    display: flex; align-items: center; height: 33px; margin-bottom: 19px;
    font-family: "Open Sans", sans-serif; font-size: 18px; color: var(--ink);
  }
  .contact-icon { width: 33px; height: 33px; margin-right: 22px; flex: none; }

  .brand-mark-front {
    position: absolute; left: 652px; top: 118px; width: 60px; height: 60px;
    border-radius: 50%; background: var(--sky);
  }
  .brand-name-front {
    position: absolute; left: 582px; top: 230px; width: 200px; text-align: center;
    font-family: "Open Sans", sans-serif; font-weight: 700; font-size: 19px;
    color: var(--navy);
  }

  .tagline {
    position: absolute; left: 356px; top: 364px;
    font-family: "PT Serif", serif; font-weight: 700; font-size: 38px;
    color: var(--navy);
  }

  .brand-mark-back {
    position: absolute; left: 333px; top: 60px; width: 150px; height: 150px;
    border-radius: 50%; background: var(--sky);
  }
  .brand-name-back {
    position: absolute; left: 0; top: 318px; width: 100%; text-align: center;
    font-family: "Open Sans", sans-serif; font-weight: 700; font-size: 44px;
    color: var(--navy); letter-spacing: -1px;
  }
</style>
</head>
<body>
<main class="canvas">

  <section class="card card-front">
    <svg class="wave-area" viewBox="0 0 806 466" preserveAspectRatio="none" role="img" aria-label="Decorative flowing blue wave artwork">
      <defs>
        <linearGradient id="waveFill" x1="0" y1="0" x2="1" y2="1">
          <stop offset="0" stop-color="#0356e0"/>
          <stop offset="0.5" stop-color="#2f7ff9"/>
          <stop offset="1" stop-color="#2f86ee"/>
        </linearGradient>
      </defs>
      <path d="M0 0 H286 C200 70 190 300 440 466 H0 Z" fill="url(#waveFill)"/>
    </svg>

    <ul class="contact-list">
      <li class="contact-item">
        <svg class="contact-icon" viewBox="0 0 34 34" aria-hidden="true">
          <circle cx="17" cy="17" r="17" fill="var(--royal)"/>
          <rect x="9" y="11" width="16" height="12" rx="1" fill="#fff"/>
          <path d="M9 11 L17 18 L25 11" stroke="var(--royal)" stroke-width="1.6" fill="none"/>
        </svg>
        hello@lodgebridgely.net
      </li>
      <li class="contact-item">
        <svg class="contact-icon" viewBox="0 0 34 34" aria-hidden="true">
          <circle cx="17" cy="17" r="17" fill="var(--royal)"/>
          <path d="M11 9 C9 12 10 18 14 22 C18 26 23 26 25 24 L22 20 L19 21 C17 20 14 17 13 15 L14 12 Z" fill="#fff"/>
        </svg>
        000 000 000 0000
      </li>
      <li class="contact-item">
        <svg class="contact-icon" viewBox="0 0 34 34" aria-hidden="true">
          <circle cx="17" cy="17" r="17" fill="var(--royal)"/>
          <path d="M17 8 C13 8 11 11 11 14 C11 18 17 25 17 25 C17 25 23 18 23 14 C23 11 21 8 17 8 Z" fill="#fff"/>
          <circle cx="17" cy="14" r="2.3" fill="var(--royal)"/>
        </svg>
        anddress, city
      </li>
      <li class="contact-item">
        <svg class="contact-icon" viewBox="0 0 34 34" aria-hidden="true">
          <circle cx="17" cy="17" r="17" fill="var(--royal)"/>
          <circle cx="17" cy="17" r="9" fill="none" stroke="#fff" stroke-width="1.8"/>
          <path d="M8 17 H26 M17 8 C13 12 13 22 17 26 M17 8 C21 12 21 22 17 26" stroke="#fff" stroke-width="1.5" fill="none"/>
        </svg>
        www.lodgebridgely.net
      </li>
    </ul>

    <div class="brand-mark-front"></div>
    <p class="brand-name-front">LodgeBridgely</p>

    <p class="tagline">Young and Memorable</p>
  </section>

  <section class="card card-back">
    <div class="brand-mark-back"></div>
    <p class="brand-name-back">LodgeBridgely.net</p>
  </section>

</main>
</body>
</html>
```